Ambo postcard design

I am in charge of getting a postcard 5x7 designed for 14 artists having a gallery exhibition. We would like to use our
photo(s) with the 14 names on the front. Back of card would have gallery information.
Am sending jpeg of a past card, four images to choose from and the text for back of card.

```html
<!DOCTYPE html>
<html lang="en">
<head>
<meta charset="utf-8">
<title>Fourteen Painters – Exhibition Postcard</title>
<link rel="stylesheet" href="https://fonts.googleapis.com/css2?family=Dancing+Script:wght@500&family=Nunito:wght@900&display=swap">
<style>
  :root {
    --card-white: #ffffff;
    --wood-dark: #3a1c0c;
    --wood-mid: #6b3418;
    --wood-light: #8a4a26;
    --floor-light: #a65e34;
    --linen: #a9a9a9;
    --linen-light: #c4c4c4;
    --text-light: #ffffff;
    --splash-yellow: #f2c81a;
    --splash-red: #d8231f;
    --splash-blue: #3b6fd1;
    --splash-ink: #141414;
    --splash-paper: #e8e6e1;
  }
  * { margin: 0; padding: 0; box-sizing: border-box; }
  html, body { width: 1200px; height: 863px; overflow: hidden; background: var(--card-white); }
  .postcard {
    position: relative;
    width: 1200px; height: 863px;
    background: var(--card-white);
  }
  .postcard__stage {
    position: absolute;
    left: 21px; top: 21px; width: 1158px; height: 821px;
    overflow: hidden;
    background:
      repeating-linear-gradient(90deg, rgba(0,0,0,0.18) 0 3px, transparent 3px 22px, rgba(255,255,255,0.05) 22px 26px, transparent 26px 57px),
      linear-gradient(90deg, var(--wood-dark), var(--wood-mid) 30%, var(--wood-light) 50%, var(--wood-mid) 70%, var(--wood-dark));
  }
  .postcard__floor {
    position: absolute;
    left: 0; top: 607px; width: 100%; height: 214px;
    background:
      radial-gradient(ellipse at 50% 0%, var(--floor-light), var(--wood-mid) 55%, var(--wood-dark));
  }
  .postcard__band {
    position: absolute;
    left: 0; top: 176px; width: 100%; height: 278px;
    background:
      repeating-linear-gradient(0deg, rgba(255,255,255,0.08) 0 1px, transparent 1px 3px),
      linear-gradient(var(--linen-light), var(--linen));
    box-shadow: 0 2px 6px rgba(0,0,0,0.4);
  }
  .artwork {
    position: absolute;
    box-shadow: 4px 6px 12px rgba(0,0,0,0.55);
    border: 2px solid rgba(255,255,255,0.6);
  }
  .artwork--light {
    background:
      radial-gradient(circle at 30% 40%, rgba(242,200,26,0.45), transparent 40%),
      radial-gradient(circle at 70% 65%, rgba(59,111,209,0.4), transparent 45%),
      radial-gradient(circle at 55% 20%, rgba(216,35,31,0.35), transparent 35%),
      linear-gradient(135deg, var(--splash-paper), #cfcac0);
  }
  .artwork--dark {
    background:
      radial-gradient(circle at 30% 30%, var(--splash-yellow), transparent 45%),
      radial-gradient(circle at 70% 70%, var(--splash-red), transparent 40%),
      radial-gradient(circle at 65% 25%, var(--splash-blue), transparent 35%),
      linear-gradient(135deg, #2b2b2b, var(--splash-ink));
  }
  .artwork--top-left   { left: 63px;  top: 116px; width: 317px; height: 182px; }
  .artwork--bottom-left{ left: 63px;  top: 310px; width: 317px; height: 203px; }
  .artwork--feature    { left: 416px; top: 51px;  width: 325px; height: 527px; }
  .artwork--top-right  { left: 773px; top: 116px; width: 318px; height: 182px; }
  .artwork--bottom-right{ left: 773px; top: 312px; width: 318px; height: 202px; }
  .exhibition {
    position: absolute;
    left: 0; top: 652px; width: 100%;
    text-align: center;
    color: var(--text-light);
  }
  .exhibition__title {
    font-family: "Dancing Script", cursive;
    font-weight: 500;
    font-size: 46px;
    line-height: 1;
    margin-bottom: 16px;
    text-shadow: 1px 2px 3px rgba(0,0,0,0.5);
  }
  .exhibition__artists {
    font-family: "Nunito", sans-serif;
    font-weight: 900;
    font-size: 29px;
    line-height: 36px;
    letter-spacing: 0.3px;
    text-shadow: 1px 2px 3px rgba(0,0,0,0.5);
  }
</style>
</head>
<body>
<div class="postcard">
  <div class="postcard__stage">
    <div class="postcard__floor"></div>
    <div class="postcard__band"></div>

    <div class="artwork artwork--light artwork--top-left" role="img" aria-label="Drip painting on white with a paint tube and brushes"></div>
    <div class="artwork artwork--light artwork--bottom-left" role="img" aria-label="Colourful drip lines on white with a wide brush and palette knife"></div>
    <div class="artwork artwork--dark artwork--feature" role="img" aria-label="Bold yellow, red and blue paint pours on black with flat brushes"></div>
    <div class="artwork artwork--dark artwork--top-right" role="img" aria-label="Poured paint on black with a brush and palette knife"></div>
    <div class="artwork artwork--dark artwork--bottom-right" role="img" aria-label="Paint pours with a yellow paint tube and brushes"></div>

    <div class="exhibition">
      <h1 class="exhibition__title">Fourteen Painters</h1>
      <p class="exhibition__artists">Hollin | Marwick | Pellowe | Dorran | Vance | Ashfield<br>Torrin | Lune | Brenner | Fenwold | Ostrand | Pemble | Kell | Wrayburn</p>
    </div>
  </div>
</div>
</body>
</html>
```